Bakery Business Cards

We are in need of business cards for our bakery business--something non-generic that reflects our business and will stand out. We are a wholesale bakery that primarily services in-store bakeries, casinos, schools, distributors, and fund-raising companies. The family business was founded in 1960. (www.dorvalbakehouse.example)

```html
<!DOCTYPE html>
<html lang="en">
<head>
<meta charset="utf-8">
<title>Dorval Bakehouse — Business Card</title>
<link href="https://fonts.googleapis.com/css2?family=Montserrat:wght@400;500;700&display=swap" rel="stylesheet">
<style>
  :root {
    --backdrop: #a8a8a8;
    --card-white: #ffffff;
    --brand-blue: #2a4e9e;
    --rule-navy: #27375f;
    --ink: #333333;
    --faint-blue: #eef0f8;
  }
  * { margin: 0; padding: 0; box-sizing: border-box; }
  html, body {
    width: 900px; height: 1200px; overflow: hidden;
    background: var(--backdrop);
    font-family: "Montserrat", sans-serif;
  }
  .canvas { position: relative; width: 900px; height: 1200px; }
  .card {
    position: absolute; left: 80px; width: 742px; height: 440px; overflow: hidden;
  }
  .card--front { top: 130px; background: var(--card-white); }
  .card--back { top: 638px; background: var(--brand-blue); }

  .faint-mark {
    position: absolute; left: 400px; top: 10px; width: 420px; height: 380px;
    border-radius: 50%; background: var(--faint-blue);
  }
  .wordmark {
    position: absolute; font-weight: 700; line-height: 1.1; color: var(--brand-blue);
  }
  .card--front .wordmark { left: 40px; top: 68px; font-size: 38px; width: 320px; }
  .card--back .wordmark {
    left: 0; right: 0; top: 150px; text-align: center; font-size: 56px; color: var(--card-white);
  }

  .person-name {
    position: absolute; left: 40px; top: 288px; font-size: 26px; font-weight: 700; color: var(--brand-blue);
  }
  .job-title {
    position: absolute; right: 42px; top: 298px; font-size: 16px; color: var(--ink);
  }
  .divider {
    position: absolute; left: 40px; right: 42px; top: 322px; height: 1.5px; background: var(--rule-navy);
  }
  .contact-list {
    position: absolute; left: 42px; top: 340px; list-style: none; font-size: 16px; color: var(--ink);
  }
  .contact-list li { display: flex; align-items: center; height: 23px; }
  .contact-list svg { width: 14px; height: 14px; margin-right: 11px; fill: var(--brand-blue); }
  .address {
    position: absolute; left: 483px; top: 365px; font-size: 16px; line-height: 23px; color: var(--ink);
  }
</style>
</head>
<body>
<main class="canvas">
  <section class="card card--front">
    <div class="faint-mark" aria-hidden="true"></div>
    <div class="wordmark">Dorval Bakehouse</div>
    <h1 class="person-name">Milo Hartman</h1>
    <p class="job-title">Operation Manager</p>
    <div class="divider"></div>
    <ul class="contact-list">
      <li>
        <svg viewBox="0 0 16 16"><path d="M2 6c0-2 2-3 6-3s6 1 6 3v1h-3V5.5H5V7H2zM4 8h8l1 5H3z"/></svg>
        (555) 014-2290
      </li>
      <li>
        <svg viewBox="0 0 16 16"><path d="M1 3h14v2L8 9 1 5zM1 6.5l7 4 7-4V13H1z"/></svg>
        sales@dorvalbakehouse.example
      </li>
      <li>
        <svg viewBox="0 0 16 16"><circle cx="8" cy="8" r="7"/></svg>
        www.dorvalbakehouse.example
      </li>
    </ul>
    <address class="address" style="font-style:normal">1187 Mercer Lane,<br>Fairview City, ST 00000</address>
  </section>

  <section class="card card--back">
    <div class="wordmark">Dorval Bakehouse</div>
  </section>
</main>
</body>
</html>
```